Music Festival Business Cards

The Lantern Gathering
Produced by Bramblewood Sound Collective LLC
New music festival in Arkansas.

Target Market(s)

18-35 year olds

Industry/Entity Type

Festival

Contact Information for Business Card

We are a 5-partner team producing a music festival in Arkansas. We need slick business cards, and I want them to be square.

Requirements
Must have
• I NEED THESE TO BE IN SQUARE SIZE - 2x2 or 2.5x2.5... please not regular size.
• I need www.lanternmeet.example as the link to website.

```html
<!DOCTYPE html>
<html lang="en">
<head>
<meta charset="utf-8">
<title>The Lantern Gathering – Business Card</title>
<link href="https://fonts.googleapis.com/css2?family=Roboto:wght@400;500;700&display=swap" rel="stylesheet">
<style>
  :root {
    --backdrop: #2b2c2f;
    --teal: #47c3cc;
    --charcoal: #23272b;
    --white: #ffffff;
    --ink: #111314;
    --text-soft: #e6e8ea;
  }
  * { margin: 0; padding: 0; box-sizing: border-box; }
  html, body {
    width: 1200px;
    height: 800px;
    overflow: hidden;
    background: var(--backdrop);
    font-family: "Roboto", Arial, sans-serif;
  }
  .sheet {
    width: 1200px;
    height: 800px;
    display: flex;
    align-items: center;
    justify-content: center;
    gap: 80px;
  }
  .card {
    position: relative;
    width: 440px;
    height: 440px;
    border-radius: 30px;
    overflow: hidden;
    box-shadow: 0 10px 28px rgba(0,0,0,0.45);
  }
  /* Front */
  .card-front {
    background: var(--teal);
    display: flex;
    align-items: center;
    justify-content: center;
    gap: 14px;
  }
  .brand-mark {
    width: 22px;
    height: 22px;
    background: var(--ink);
  }
  .brand-name {
    color: var(--ink);
    font-weight: 700;
    font-size: 30px;
    letter-spacing: 0.5px;
  }
  /* Back */
  .card-back { background: var(--teal); }
  .card-back .swoosh {
    position: absolute;
    inset: 0;
    width: 100%;
    height: 100%;
  }
  .contact {
    position: absolute;
    top: 48px;
    right: 48px;
    width: 260px;
    text-align: right;
    color: var(--text-soft);
  }
  .contact-name {
    color: var(--white);
    font-weight: 700;
    font-size: 20px;
    letter-spacing: 1px;
    text-transform: uppercase;
  }
  .contact-role {
    color: var(--teal);
    font-size: 15px;
    font-weight: 500;
    margin-top: 2px;
  }
  .contact-rule {
    height: 1px;
    background: var(--teal);
    opacity: 0.8;
    margin: 11px 0 9px;
  }
  .contact-label {
    color: var(--teal);
    font-size: 12px;
    font-weight: 700;
  }
  .contact-value {
    font-size: 15px;
    line-height: 1.35;
  }
</style>
</head>
<body>
<main class="sheet">
  <section class="card card-front" aria-label="Card front">
    <span class="brand-mark"></span>
    <span class="brand-name">The Lantern Gathering</span>
  </section>

  <section class="card card-back" aria-label="Card back">
    <svg class="swoosh" viewBox="0 0 440 440" aria-hidden="true">
      <path d="M0,0 H440 V440 H300 C160,425 30,330 0,170 Z" fill="var(--charcoal)"/>
      <path d="M-2,180 C32,335 165,428 296,446" fill="none" stroke="var(--white)" stroke-width="6"/>
    </svg>
    <div class="contact">
      <p class="contact-name">Rowan Ellery</p>
      <p class="contact-role">Manager</p>
      <div class="contact-rule"></div>
      <p class="contact-label">Phone</p>
      <p class="contact-value">(479) 555-0142</p>
      <div class="contact-rule"></div>
      <p class="contact-label">E-mail</p>
      <p class="contact-value">hello@lanternmeet.example</p>
      <div class="contact-rule"></div>
      <p class="contact-label">Web</p>
      <p class="contact-value">www.lanternmeet.example</p>
      <div class="contact-rule"></div>
      <p class="contact-value">PO Box 48 Lantern Row<br>Fayetteville, Arkansas</p>
    </div>
  </section>
</main>
</body>
</html>
```